Business Card Design and New Company Logo

I need a business card design and new company logo for a plant nursery. I will be propagating landscape plants from cuttings and growing them locally for resale, locally grown and nurtured plants for zone 5 climate. I would like a design that depicts the growth of shoots to roots .... locally grown and nurtured landscape plants. Healthy, hardy ornamental trees and shrubs for $4.97. Affordable gardening for all.
Updates
Hello Designers,
Thank you for your submissions. I am going to be out of my office until Monday. I will continue to review submitted designs when I can and posting requests for revisions when time permits on my business trip. I should have a decision next week.
Sincerely,
Marla
Sorry for my delay in choosing a design. I had some unforeseen business and personal events culminate at the same time. I will have my decision by the end of this week and update all by Friday March 21. Thank you for your design submissions and your patience.
Marla
Target Market(s)
Home owners
Industry/Entity Type
Landscape
Contact Information for Business Card
Fernbrook Hollow Nursery
Marla Dunwick
812 Calder Pond Lane
Marrowvale, MA 01077
413-862-3094
Fernbrook4Hollow@mailvine.net
Look and feel
Each slider illustrates characteristics of the customer's brand and the style your logo design should communicate.

```html
<!DOCTYPE html>
<html lang="en">
<head>
<meta charset="utf-8">
<title>Fernbrook Hollow Nursery — Business Card</title>
<link href="https://fonts.googleapis.com/css2?family=Open+Sans:wght@400;600;700&family=Dancing+Script:wght@400&display=swap" rel="stylesheet">
<style>
  :root {
    --page-bg: #e4e4e4;
    --leaf-green: #35753a;
    --paper-white: #ffffff;
    --mist-light: #fafafa;
    --mist-dark: #d6d6d6;
    --sky-blue: #5aa0dc;
    --sky-pale: #cfe2f3;
  }
  * { box-sizing: border-box; margin: 0; padding: 0; }
  html, body {
    width: 1200px; height: 900px; overflow: hidden;
    background: var(--page-bg);
    font-family: "Open Sans", Arial, sans-serif;
  }
  .canvas {
    position: relative; width: 1200px; height: 900px;
    display: flex; align-items: center; justify-content: center; gap: 40px;
  }
  .card {
    position: relative; width: 500px; height: 286px; overflow: hidden;
    box-shadow: 0 3px 10px rgba(0,0,0,0.18);
  }
  /* Front */
  .card-front {
    background: var(--leaf-green);
    display: flex; align-items: center; justify-content: center;
  }
  .wordmark { font-weight: 600; text-align: center; line-height: 1.1; }
  .card-front .wordmark { color: var(--paper-white); font-size: 40px; }
  /* Back */
  .card-back { background: var(--leaf-green); }
  .back-top {
    position: absolute; left: 0; top: 0; width: 100%; height: 108px;
    background: radial-gradient(ellipse at 65% 50%, var(--mist-light) 0%, #eeeeee 55%, var(--mist-dark) 100%);
    display: flex; align-items: center; justify-content: center;
    padding-left: 110px;
  }
  .card-back .wordmark { color: var(--leaf-green); font-size: 28px; }
  .back-stripe {
    position: absolute; left: 0; top: 108px; width: 100%; height: 7px;
    background: linear-gradient(to bottom, var(--sky-blue), var(--sky-pale));
  }
  .contact-person {
    position: absolute; left: 34px; top: 132px; color: var(--paper-white);
  }
  .person-name {
    font-family: "Dancing Script", cursive; font-size: 26px; font-weight: 400;
    margin-bottom: 4px;
  }
  .contact-line { font-size: 13px; line-height: 1.45; }
  .company-block {
    position: absolute; right: 30px; bottom: 34px; color: var(--paper-white);
    font-size: 13px; line-height: 1.45; font-style: normal;
  }
  .company-name { font-weight: 700; }
</style>
</head>
<body>
<main class="canvas">
  <section class="card card-front" aria-label="Card front">
    <div class="wordmark">Fernbrook Hollow<br>Nursery</div>
  </section>

  <section class="card card-back" aria-label="Card back">
    <div class="back-top">
      <div class="wordmark">Fernbrook Hollow<br>Nursery</div>
    </div>
    <div class="back-stripe"></div>
    <div class="contact-person">
      <p class="person-name">Marla Dunwick</p>
      <p class="contact-line">413-862-3094</p>
      <p class="contact-line">Fernbrook4Hollow@mailvine.net</p>
    </div>
    <address class="company-block">
      <p class="company-name">Fernbrook Hollow Nursery</p>
      <p>812 Calder Pond Lane</p>
      <p>Marrowvale, MA 01077</p>
    </address>
  </section>
</main>
</body>
</html>
```